Design a Retail Box for Industrial Welding Helmets

We are excited to launch a design contest for our product's new retail packaging.
The products are 2 welding helmets.
Product 1 is Brontal helmet and product 2 is Veltrix helmet.
We are seeking for :
A) 1 main design of the box with minor adjustments for the 2 different models (Brontal and Veltrix)
B) 1 design for the sticker of Brontal (font)
C)1 design for the sticker of Veltrix (font)
Attached you will find:
1)Brand logo
2)Reference of welding wire packaging
3)Reference of welding torch packaging
4)Photo of Brontal model
5)Data of Brontal model to be included
6)Photo of Veltrix model
7)Data of Veltrix model to be included
8)Dieline Template of the box in .ai and .jpg
9)Vectors for the different uses of the helmets
Your design should reflect our brand and communicate the product's value while standing out on retail shelves.
The winner will be selected based on creativity, brand alignment, and overall design aesthetics.
We look forward to seeing your creative concepts.
Target Market(s)
Industrial and Retail
Industry/Entity Type
Welding, Retail, Hardware
Colors
Designer to choose colors to be used in the design.
Look and feel
Each slider illustrates characteristics of the customer's brand and the style your logo design should communicate.

```html
<!DOCTYPE html>
<html lang="en">
<head>
<meta charset="utf-8">
<title>Korven Welding Helmet Retail Box – Veltrix &amp; Brontal</title>
<link href="https://fonts.googleapis.com/css2?family=Exo+2:wght@600;800&family=Roboto:wght@400;700&display=swap" rel="stylesheet">
<style>
  :root{
    --orange:#ff5a00;
    --box-dark:#2c2c2e;
    --box-mid:#3b3b3e;
    --stripe:#4a4a4d;
    --ghost-text:#57575a;
    --card-light:#e9e9ea;
    --card-ink:#333;
    --label-gold:#e6a100;
    --bg-light:#8a8a8b;
    --bg-dark:#4a4a4c;
    --white:#fff;
  }
  html,body{margin:0;padding:0;width:1200px;height:901px;overflow:hidden}
  .stage{position:relative;width:1200px;height:901px;display:flex}
  .half{width:600px;height:901px;position:relative}
  .half--veltrix{background:var(--bg-light)}
  .half--brontal{background:var(--bg-dark)}
  .dieline{position:absolute;left:23px;top:218px;width:553px;height:466px}
  .title{font-family:"Exo 2",sans-serif;font-weight:800;letter-spacing:1.2px;fill:var(--orange)}
  .ghost{font-family:"Exo 2",sans-serif;font-weight:800;letter-spacing:.8px;fill:var(--ghost-text)}
  .brand{font-family:"Exo 2",sans-serif;font-weight:600;letter-spacing:1.5px}
  .small{font-family:Roboto,sans-serif;font-weight:400}
  .small-bold{font-family:Roboto,sans-serif;font-weight:700}
</style>
</head>
<body>
<main class="stage">

  <!-- Veltrix box net -->
  <section class="half half--veltrix">
    <svg class="dieline" viewBox="0 0 395 333" xmlns="http://www.w3.org/2000/svg">
      <defs>
        <linearGradient id="bandV" x1="0" y1="0" x2="0" y2="1">
          <stop offset="0" stop-color="#3a3a3d"/><stop offset="1" stop-color="#232325"/>
        </linearGradient>
        <radialGradient id="helmetV" cx=".45" cy=".4" r=".6">
          <stop offset="0" stop-color="#5a5a60"/><stop offset=".6" stop-color="#1e1e22"/><stop offset="1" stop-color="#0e0e10"/>
        </radialGradient>
      </defs>
      <!-- top flap -->
      <rect class="flap-top" x="98" y="0" width="100" height="97" fill="var(--orange)"/>
      <rect x="141" y="22" width="14" height="14" fill="var(--box-dark)"/>
      <text class="brand" x="148" y="58" font-size="16" text-anchor="middle" fill="var(--box-dark)">KORVEN</text>
      <text class="small-bold" x="148" y="68" font-size="5.5" text-anchor="middle" fill="var(--box-dark)" letter-spacing=".6">WELDING FORGE</text>
      <!-- body band -->
      <rect x="0" y="97" width="395" height="138" fill="url(#bandV)"/>
      <g fill="var(--stripe)" opacity=".7">
        <polygon points="60,235 110,150 116,150 66,235"/>
        <polygon points="250,235 300,150 306,150 256,235"/>
        <polygon points="355,235 395,168 395,178 361,235"/>
      </g>
      <g fill="var(--orange)">
        <rect x="0" y="145" width="26" height="32"/>
        <rect x="74" y="145" width="30" height="32"/>
        <rect x="198" y="145" width="28" height="32"/>
        <rect x="258" y="145" width="38" height="32"/>
      </g>
      <!-- side 1 spec card -->
      <rect x="22" y="113" width="56" height="107" fill="var(--card-light)" stroke="#bbb" stroke-width=".6"/>
      <g class="small" font-size="3.6" fill="var(--card-ink)">
        <circle cx="30" cy="125" r="4" fill="#444"/><text x="37" y="124">Large 100x65 mm view</text>
        <text x="54" y="131" class="small-bold" fill="var(--label-gold)">SENSITIVITY</text>
        <circle cx="30" cy="148" r="4" fill="#444"/><text x="37" y="147">Solar power cell</text>
        <text x="60" y="155" class="small-bold" fill="var(--label-gold)">DELAY</text>
        <circle cx="30" cy="172" r="4" fill="#444"/><text x="37" y="173">Shade 9-13 range</text>
        <circle cx="30" cy="198" r="4" fill="#444"/><text x="37" y="199">Grind mode switch</text>
      </g>
      <!-- front -->
      <text class="title" x="105" y="108" font-size="9">VELTRIX</text>
      <rect x="176" y="99" width="19" height="22" fill="var(--orange)"/>
      <text class="brand" x="185.5" y="113" font-size="4" text-anchor="middle" fill="var(--white)">KORVEN</text>
      <ellipse role="img" aria-label="Photo of the Veltrix welding helmet, front view" cx="151" cy="166" rx="30" ry="38" fill="url(#helmetV)"/>
      <text class="ghost" x="148" y="229" font-size="7.5" text-anchor="middle">WELDING HELMET</text>
      <!-- side 2 spec panel -->
      <rect x="220" y="113" width="42" height="107" fill="#111" stroke="var(--white)" stroke-width=".8"/>
      <text class="small-bold" x="241" y="122" font-size="4.4" text-anchor="middle" fill="var(--white)">Large View</text>
      <text class="small-bold" x="241" y="128" font-size="4.4" text-anchor="middle" fill="var(--orange)">Welding Helmet</text>
      <g class="small" font-size="3.4" fill="#ccc" text-anchor="middle">
        <text x="241" y="142">Wide view</text>
        <text x="241" y="158">Auto darkening</text>
        <text x="241" y="174">True color</text>
        <text x="241" y="190">Grind mode</text>
        <text x="241" y="212">Shade 4/9-13</text>
      </g>
      <!-- back -->
      <text class="ghost" x="345" y="120" font-size="7.5" text-anchor="middle">WELDING HELMET</text>
      <ellipse role="img" aria-label="Photo of the Veltrix welding helmet, angled view" cx="345" cy="168" rx="30" ry="37" fill="url(#helmetV)"/>
      <rect x="370" y="210" width="20" height="22" fill="var(--orange)"/>
      <text class="brand" x="380" y="224" font-size="4" text-anchor="middle" fill="var(--white)">KORVEN</text>
      <!-- bottom flap -->
      <rect x="98" y="235" width="100" height="98" fill="var(--box-dark)"/>
    </svg>
  </section>

  <!-- Brontal box net -->
  <section class="half half--brontal">
    <svg class="dieline" viewBox="0 0 395 333" xmlns="http://www.w3.org/2000/svg">
      <defs>
        <linearGradient id="bandB" x1="0" y1="0" x2="0" y2="1">
          <stop offset="0" stop-color="#3a3a3d"/><stop offset="1" stop-color="#232325"/>
        </linearGradient>
        <radialGradient id="helmetB" cx=".45" cy=".4" r=".6">
          <stop offset="0" stop-color="#55555b"/><stop offset=".6" stop-color="#1b1b1f"/><stop offset="1" stop-color="#0c0c0e"/>
        </radialGradient>
      </defs>
      <rect x="98" y="0" width="100" height="97" fill="var(--box-dark)"/>
      <rect x="141" y="22" width="14" height="14" fill="#6a6a6d"/>
      <text class="brand" x="148" y="58" font-size="16" text-anchor="middle" fill="#8a8a8d">KORVEN</text>
      <text class="small-bold" x="148" y="68" font-size="5.5" text-anchor="middle" fill="#8a8a8d" letter-spacing=".6">WELDING FORGE</text>
      <rect x="0" y="97" width="395" height="138" fill="url(#bandB)"/>
      <g fill="var(--stripe)" opacity=".7">
        <polygon points="60,235 110,150 116,150 66,235"/>
        <polygon points="250,235 300,150 306,150 256,235"/>
        <polygon points="355,235 395,168 395,178 361,235"/>
      </g>
      <g fill="var(--orange)">
        <rect x="0" y="145" width="26" height="32"/>
        <rect x="74" y="145" width="30" height="32"/>
        <rect x="198" y="145" width="28" height="32"/>
        <rect x="258" y="145" width="38" height="32"/>
      </g>
      <rect x="22" y="113" width="56" height="107" fill="var(--card-light)" stroke="#bbb" stroke-width=".6"/>
      <g class="small" font-size="3.6" fill="var(--card-ink)">
        <circle cx="30" cy="125" r="4" fill="#444"/><text x="37" y="124">Large 100x65 mm view</text>
        <text x="54" y="131" class="small-bold" fill="var(--label-gold)">SENSITIVITY</text>
        <circle cx="30" cy="148" r="4" fill="#444"/><text x="37" y="147">Solar power cell</text>
        <text x="60" y="155" class="small-bold" fill="var(--label-gold)">DELAY</text>
        <circle cx="30" cy="172" r="4" fill="#444"/><text x="37" y="173">Shade 9-13 range</text>
        <circle cx="30" cy="198" r="4" fill="#444"/><text x="37" y="199">Grind mode switch</text>
      </g>
      <text class="title" x="105" y="108" font-size="9">BRONTAL</text>
      <rect x="176" y="99" width="19" height="22" fill="var(--orange)"/>
      <text class="brand" x="185.5" y="113" font-size="4" text-anchor="middle" fill="var(--white)">KORVEN</text>
      <ellipse role="img" aria-label="Photo of the Brontal welding helmet, front view" cx="151" cy="166" rx="31" ry="37" fill="url(#helmetB)"/>
      <text class="ghost" x="148" y="229" font-size="7.5" text-anchor="middle">WELDING HELMET</text>
      <rect x="220" y="113" width="42" height="107" fill="#111" stroke="var(--white)" stroke-width=".8"/>
      <text class="small-bold" x="241" y="122" font-size="4.4" text-anchor="middle" fill="var(--white)">Large View</text>
      <text class="small-bold" x="241" y="128" font-size="4.4" text-anchor="middle" fill="var(--orange)">Welding Helmet</text>
      <g class="small" font-size="3.4" fill="#ccc" text-anchor="middle">
        <text x="241" y="142">Wide view</text>
        <text x="241" y="158">Auto darkening</text>
        <text x="241" y="174">True color</text>
        <text x="241" y="190">Grind mode</text>
        <text x="241" y="212">Shade 4/9-13</text>
      </g>
      <text class="ghost" x="345" y="120" font-size="7.5" text-anchor="middle">WELDING HELMET</text>
      <ellipse role="img" aria-label="Photo of the Brontal welding helmet, angled view" cx="345" cy="168" rx="29" ry="36" fill="url(#helmetB)"/>
      <rect x="370" y="210" width="20" height="22" fill="var(--orange)"/>
      <text class="brand" x="380" y="224" font-size="4" text-anchor="middle" fill="var(--white)">KORVEN</text>
      <rect x="98" y="235" width="100" height="98" fill="var(--box-dark)"/>
    </svg>
  </section>

</main>
</body>
</html>
```